Energy trading company (Voltrisa) needs a business card

We need a business card for a company based in Central America. Our main purpose is trading energy . We already have the logo but we need some good creativity to design a high impact business card. Colors blue, orange, green can be used or we would like to see good combinatios with our logo

Target Market(s)

Energy

Industry/Entity Type

Power Generation

Contact Information for Business Card

Logo , headquarters , name, background

Font styles to use
Serif
Sans Serif

Colors

Designer to choose colors to be used in the design.

Requirements
Must have
• it must have a fresh and clean view
Nice to have
• good backgrounds that combine with the logo
Should not have
• too much words

```html
<!DOCTYPE html>
<html lang="en">
<head>
<meta charset="utf-8">
<title>Voltrisa business card</title>
<link href="https://fonts.googleapis.com/css2?family=Mulish:wght@400;600;700&display=swap" rel="stylesheet">
<style>
  :root {
    --page: #1f2328;
    --card-blue: #2d5573;
    --card-white: #ffffff;
    --accent-orange: #f7931e;
    --text-light: #e6edf3;
  }
  html, body {
    margin: 0;
    width: 1200px;
    height: 900px;
    overflow: hidden;
    background: var(--page);
    font-family: "Mulish", sans-serif;
  }
  .canvas {
    position: relative;
    width: 1200px;
    height: 900px;
  }
  .card {
    position: absolute;
    left: 260px;
    width: 680px;
    height: 408px;
    box-shadow: 0 14px 34px rgba(0,0,0,0.45);
    overflow: hidden;
  }
  .card-front { top: 30px; background: var(--card-white); }
  .card-back { top: 462px; background: var(--card-blue); }
  .card svg { display: block; }

  .brand {
    position: absolute;
    display: flex;
    align-items: center;
    gap: 12px;
    color: var(--accent-orange);
    font-weight: 600;
    letter-spacing: 1px;
    text-transform: uppercase;
  }
  .brand-dot {
    border-radius: 50%;
    background: var(--accent-orange);
  }
  .card-front .brand { left: 44px; top: 42px; font-size: 40px; }
  .card-front .brand-dot { width: 30px; height: 30px; }
  .card-back .brand {
    left: 0; right: 0; top: 0; bottom: 0;
    justify-content: center;
    font-size: 48px;
  }
  .card-back .brand-dot { width: 36px; height: 36px; }

  .contact {
    position: absolute;
    right: 34px;
    bottom: 30px;
    text-align: right;
    color: var(--text-light);
    font-size: 15px;
    line-height: 25px;
  }
  .contact-name {
    color: var(--accent-orange);
    font-weight: 700;
    font-size: 22px;
    letter-spacing: 1.5px;
    text-transform: uppercase;
    margin-bottom: 6px;
  }
  .contact-line {
    display: flex;
    justify-content: flex-end;
    align-items: center;
    gap: 10px;
  }
  .contact-icon { width: 16px; height: 16px; flex: none; }
  .contact-icon-spacer { width: 16px; flex: none; }
</style>
</head>
<body>
<main class="canvas">

  <section class="card card-front" aria-label="Card front">
    <svg class="front-wave" width="680" height="408" viewBox="0 0 680 408">
      <path d="M0 300 C 170 400, 300 290, 420 250 C 530 215, 620 140, 680 110 L680 408 L0 408 Z" fill="var(--card-blue)"/>
      <path d="M40 300 C 170 395, 300 282, 420 242 C 530 206, 615 130, 680 98" fill="none" stroke="var(--card-white)" stroke-width="8"/>
      <path d="M26 285 C 165 385, 300 268, 420 228 C 530 192, 612 118, 680 84" fill="none" stroke="var(--accent-orange)" stroke-width="7"/>
      <path d="M70 300 C 180 365, 290 262, 400 226" fill="none" stroke="var(--accent-orange)" stroke-width="3"/>
    </svg>

    <div class="brand"><span class="brand-name">Voltrisa</span><span class="brand-dot"></span></div>

    <div class="contact">
      <div class="contact-name">Marta Solano</div>
      <div class="contact-line">+506 2290 4410
        <svg class="contact-icon" viewBox="0 0 16 16"><path d="M3 1.5l3 0.5 1 3.5-2 1.2c0.9 2 2.3 3.4 4.3 4.3L10.5 9l3.5 1 0.5 3c-0.5 1.2-1.5 1.8-2.6 1.6C6.6 13.8 2.2 9.4 1.4 4.1 1.2 3 1.8 2 3 1.5z" fill="var(--accent-orange)"/></svg>
      </div>
      <div class="contact-line">info@voltrisa.com
        <svg class="contact-icon" viewBox="0 0 16 16"><rect x="1" y="3" width="14" height="10" fill="var(--accent-orange)"/><path d="M1.5 3.5L8 9l6.5-5.5" fill="none" stroke="var(--card-blue)" stroke-width="1.4"/></svg>
      </div>
      <div class="contact-line">www.voltrisa.com
        <svg class="contact-icon" viewBox="0 0 16 16"><circle cx="8" cy="8" r="7" fill="var(--accent-orange)"/><path d="M1 8h14M8 1c-3 3.5-3 10.5 0 14M8 1c3 3.5 3 10.5 0 14" fill="none" stroke="var(--card-blue)" stroke-width="1"/></svg>
      </div>
      <div class="contact-line">Paseo Colón 118, San José<span class="contact-icon-spacer"></span></div>
    </div>
  </section>

  <section class="card card-back" role="img" aria-label="Card back: deep blue field with a faint repeating brand pattern and the Voltrisa name in orange">
    <div class="brand"><span class="brand-name">Voltrisa</span><span class="brand-dot"></span></div>
  </section>

</main>
</body>
</html>
```